Visitenkarten-Design für freie Trauerrednerin
Viele Ideen, viele Vorschläge, orientiert sich an den Kundenwünschen, nimmt immer wieder Anpassungen vor, gute Kommunikation während des Projekts. Ich bin sehr zufrieden.
Zielgruppe
Ich bin Freie Trauerrednerin, also in selbständiger Tätigkeit. (Damit ist auch die Zielgruppe erklärt)
Aufgabenstellung
Das Anliegen sollte erkennbar sein und ein Foto (Naturfotografie) passender Natur sollte den ganzen Hintergrund ausfüllen. Kontaktdaten sollten wie folgt erscheinen: Name, Vorname, Telefon, E-Mail-Adresse, Anschrift mit PLZ, Ort, Straße, Hausnummer.
Auf der Vorderseite sollte nur mein Name und meine Tätigkeit stehen, auf der Rückseite nochmals Name und Tätigkeit und alle restlichen Daten.
Die hochgeladene Datei ist ein Beispiel meiner engeren Vorstellung des Designs.

```html
<!DOCTYPE html>
<html lang="de">
<head>
<meta charset="utf-8">
<title>Lena Marx – Trauerrednerin – Visitenkarte</title>
<link rel="stylesheet" href="https://fonts.googleapis.com/css2?family=Source+Sans+3:wght@300;400&display=swap">
<style>
  :root {
    --canvas: #ffffff;
    --paper: #f3f3f1;
    --forest: #1f6b3a;
    --ink: #333333;
    --white: #ffffff;
    --photo-dark: #141a16;
    --photo-mid: #23382a;
    --photo-leaf: #3f6b45;
    --photo-wing: #c8642a;
    --motif: #c9d8cf;
  }
  * { margin: 0; padding: 0; box-sizing: border-box; }
  html, body {
    width: 1200px; height: 900px; overflow: hidden;
    background: var(--canvas);
    font-family: "Source Sans 3", "Helvetica Neue", Arial, sans-serif;
  }
  .canvas { position: relative; width: 1200px; height: 900px; }

  .card {
    position: absolute; top: 203px;
    width: 435px; height: 242px;
    overflow: hidden;
    box-shadow: 0 1px 4px rgba(0,0,0,0.18);
  }
  .card--front { left: 182px; }
  .card--back { left: 639px; background: var(--paper); }

  .card__photo {
    position: absolute; inset: 0;
    background:
      radial-gradient(ellipse 18% 22% at 32% 38%, var(--photo-wing) 0%, rgba(200,100,42,0) 100%),
      radial-gradient(ellipse 45% 45% at 75% 70%, var(--photo-leaf) 0%, rgba(63,107,69,0) 100%),
      linear-gradient(135deg, var(--photo-mid) 0%, var(--photo-dark) 55%, var(--photo-mid) 100%);
  }

  .name {
    font-weight: 300;
    color: var(--forest);
    letter-spacing: 0.02em;
    white-space: nowrap;
  }
  .role {
    font-weight: 400;
    text-transform: uppercase;
    color: var(--ink);
    white-space: nowrap;
  }

  .card--front .name {
    position: absolute; left: 228px; top: 150px;
    font-size: 34px; color: var(--white);
  }
  .card--front .role {
    position: absolute; left: 245px; top: 203px;
    font-size: 8px; letter-spacing: 0.72em; color: var(--white);
  }

  .card__motif {
    position: absolute; left: 15px; top: 3px;
    width: 76px; height: 141px;
    background: radial-gradient(ellipse at 50% 45%, var(--motif) 0%, rgba(201,216,207,0) 70%);
    opacity: 0.6;
  }
  .card--back .identity {
    position: absolute; left: 0; right: 0; top: 52px;
    text-align: center;
  }
  .card--back .name { font-size: 30px; line-height: 1.2; }
  .card--back .role {
    margin-top: 2px; padding-left: 0.72em;
    font-size: 6.5px; letter-spacing: 0.72em;
  }
  .contact {
    position: absolute; left: 0; right: 0; top: 138px;
    list-style: none; text-align: center;
    font-size: 7.5px; line-height: 17px; color: var(--ink);
  }

  .brand-lockup {
    position: absolute; left: 0; right: 0; top: 700px;
    text-align: center;
  }
  .brand-lockup .name { font-size: 76px; line-height: 1.1; }
  .brand-lockup .role {
    margin-top: 6px; padding-left: 0.95em;
    font-size: 15px; letter-spacing: 0.95em;
  }
</style>
</head>
<body>
<main class="canvas">
  <section class="card card--front">
    <div class="card__photo" role="img" aria-label="Naturfotografie: orangefarbener Schmetterling auf grünen Blättern vor dunklem Hintergrund"></div>
    <p class="name">Lena Marx</p>
    <p class="role">Trauerrednerin</p>
  </section>

  <section class="card card--back">
    <div class="card__motif" role="img" aria-label="Zarte Linienzeichnung eines Schmetterlings"></div>
    <div class="identity">
      <p class="name">Lena Marx</p>
      <p class="role">Trauerrednerin</p>
    </div>
    <ul class="contact">
      <li>Birkenweg 12&nbsp; | &nbsp;07743 Jena</li>
      <li>+49 (0)151 234 56 78</li>
      <li>lena.marx@mail.de</li>
    </ul>
  </section>

  <section class="brand-lockup">
    <p class="name">Lena Marx</p>
    <p class="role">Trauerrednerin</p>
  </section>
</main>
</body>
</html>
```